Clever & creative business card needed for a pediatric dentist.

We need a business card for a pediatric dentist that is building a brand-new pediatric dental practice. He is funny, outgoing, and sociable, and he hopes to give his business card to dentists and pediatricians so that he can give them information of where to refer infants, children, and teenagers that need high quality and attainable dental care.

The name of the dental practice is Amber Creek Pediatric Dentistry. Logo design .png / .pdf/ .jpg are provided to aid in the design.

The dentist's last name is Moffat (which sounds like "burger", as in "hamburger” or “cheeseburger"). Since it is pediatric practice, kudos will be given to designs that implement a little joke into the design - but hopefully in a small or hidden way (such as putting something like a cheeseburger on the back of the card, or hiding it an an abstract way).

Thank you!

Please make a design that incorporates colors. It should be fun! Not too serious. It does not have to follow the color scheme of the logos.

```html
<!DOCTYPE html>
<html lang="en">
<head>
<meta charset="utf-8">
<title>Amber Creek Pediatric Dentistry – Business Card</title>
<link href="https://fonts.googleapis.com/css2?family=Montserrat:wght@400;500;600;700&family=Caveat:wght@500&display=swap" rel="stylesheet">
<style>
  :root {
    --bg: #2e2e2e;
    --card-dark: #3b3b3c;
    --card-dark-panel: #474a47;
    --ink-light: #ffffff;
    --ink-dark: #3d3d3d;
    --green-pale: #c4dfb5;
    --green-soft: #9ccb89;
    --green-mid: #6bb96b;
    --green-deep: #3a9a4f;
    --pill: #e9e9e9;
    --pill-ink: #444444;
  }
  * { box-sizing: border-box; margin: 0; padding: 0; }
  html, body { width: 1200px; height: 900px; overflow: hidden; }
  body {
    background: var(--bg);
    font-family: "Montserrat", Arial, sans-serif;
    position: relative;
  }
  .card {
    position: absolute;
    top: 300px;
    width: 514px;
    height: 298px;
    border-radius: 18px;
    overflow: hidden;
  }
  /* Front */
  .card-front { left: 72px; background: var(--card-dark); color: var(--ink-light); }
  .front-panel {
    position: absolute; left: 182px; top: 0; width: 332px; height: 298px;
    background: var(--card-dark-panel);
    border-top-left-radius: 160px;
  }
  .brand { position: absolute; text-align: center; }
  .brand-name { font-weight: 500; letter-spacing: 0.2px; line-height: 1; }
  .brand-sub { font-weight: 500; letter-spacing: 2.4px; text-transform: uppercase; margin-top: 4px; }
  .card-front .brand { left: 150px; top: 66px; width: 230px; }
  .card-front .brand-name { font-size: 21px; color: var(--ink-light); }
  .card-front .brand-sub { font-size: 7px; color: var(--ink-light); }
  .brand-dot {
    display: block; margin: 0 auto 8px; width: 26px; height: 26px; border-radius: 50%;
    background: var(--green-soft);
  }
  .person { position: absolute; left: 36px; top: 146px; }
  .person-name { font-size: 19px; font-weight: 500; }
  .person-title { font-size: 11px; font-weight: 600; letter-spacing: 0.4px; margin-top: 3px; }
  .contact { position: absolute; left: 258px; top: 146px; font-size: 12.5px; list-style: none; }
  .contact li { display: flex; align-items: center; gap: 7px; height: 16.5px; }
  .contact svg { width: 12px; height: 12px; fill: var(--green-mid); flex: none; }
  .address { position: absolute; left: 258px; top: 208px; font-size: 12.5px; line-height: 16.5px; }
  .appointment-label {
    position: absolute; left: 34px; top: 220px;
    font-family: "Caveat", cursive; font-size: 18px; color: var(--green-mid);
  }
  .appointment-fields {
    position: absolute; left: 32px; top: 244px; width: 466px; height: 34px;
    background: var(--pill); border-radius: 17px;
    display: flex; align-items: center; padding: 0 13px; gap: 16px;
    font-size: 12.5px; color: var(--pill-ink);
  }
  .field { display: flex; align-items: flex-end; gap: 4px; flex: 1; }
  .field-line { flex: 1; border-bottom: 1px solid #777; height: 10px; }
  /* Back */
  .card-back { left: 615px; background: #ffffff; }
  .back-pattern {
    position: absolute; left: 0; top: 0; width: 330px; height: 298px;
    background: linear-gradient(90deg, var(--green-mid) 0%, var(--green-soft) 60%, var(--green-pale) 100%);
    border-top-right-radius: 150px;
  }
  .card-back .brand { left: 338px; top: 188px; width: 160px; }
  .card-back .brand-name { font-size: 20px; color: var(--ink-dark); }
  .card-back .brand-sub { font-size: 7px; color: var(--ink-dark); }
  .card-back .brand-dot { background: var(--green-soft); }
</style>
</head>
<body>

<section class="card card-front" aria-label="Card front">
  <div class="front-panel"></div>

  <div class="brand">
    <span class="brand-dot"></span>
    <div class="brand-name">amber creek</div>
    <div class="brand-sub">Pediatric Dentistry</div>
  </div>

  <div class="person">
    <div class="person-name">Daniel Moffat</div>
    <div class="person-title">PEDIATRIC DENTIST</div>
  </div>

  <ul class="contact">
    <li><svg viewBox="0 0 24 24"><path d="M6.6 10.8a15.1 15.1 0 0 0 6.6 6.6l2.2-2.2a1 1 0 0 1 1-.25 11.4 11.4 0 0 0 3.6.57 1 1 0 0 1 1 1V20a1 1 0 0 1-1 1A17 17 0 0 1 3 4a1 1 0 0 1 1-1h3.5a1 1 0 0 1 1 1c0 1.25.2 2.45.57 3.57a1 1 0 0 1-.25 1z"/></svg>555 014 27 80</li>
    <li><svg viewBox="0 0 24 24"><path d="M2 5h20v14H2z M2 5l10 8 10-8" /></svg>info@ambercreekdentistry.com</li>
    <li><svg viewBox="0 0 24 24"><circle cx="12" cy="12" r="10"/></svg>www.ambercreekdentistry.com</li>
  </ul>

  <div class="address">48 Meadow Lane<br>Brookfield, New York 12060</div>

  <div class="appointment-label">Your Next Appointment</div>
  <div class="appointment-fields">
    <div class="field">Date <span class="field-line"></span></div>
    <div class="field">Time <span class="field-line"></span></div>
  </div>
</section>

<section class="card card-back" aria-label="Card back">
  <div class="back-pattern" role="img" aria-label="Large green brand graphic in layered greens"></div>
  <div class="brand">
    <span class="brand-dot"></span>
    <div class="brand-name">amber creek</div>
    <div class="brand-sub">Pediatric Dentistry</div>
  </div>
</section>

</body>
</html>
```